KORVELTA Corporate Business Card

Modern business card design for company which focuses in the areas of Staffing, IT Consulting & Data Services. Please note: We are no longer using the IT subscript on the logo. All designs should have IT subscript removed.
Website: www.korveltait.example

```html
<!DOCTYPE html>
<html lang="en">
<head>
<meta charset="utf-8">
<title>KORVELTA Business Card</title>
<link href="https://fonts.googleapis.com/css2?family=Open+Sans:wght@400;600&display=swap" rel="stylesheet">
<style>
  :root {
    --backdrop: #6b6b67;
    --card: #5e5e5e;
    --ink-light: #d4d4d4;
    --ink-muted: #c2c2c2;
    --brand-blue: #2e9ad8;
    --brand-deep: #1f6fb8;
  }
  * { margin: 0; padding: 0; box-sizing: border-box; }
  html, body {
    width: 1200px; height: 1200px; overflow: hidden;
    background: var(--backdrop);
    font-family: "Open Sans", sans-serif;
  }
  .card {
    position: absolute;
    background: var(--card);
  }
  .card-front { left: 337px; top: 222px; width: 526px; height: 327px; }
  .card-back  { left: 335px; top: 667px; width: 530px; height: 333px; }

  .front-brand {
    position: absolute; left: 118px; top: 118px;
    display: flex; align-items: center; gap: 8px;
  }
  .brand-square {
    width: 16px; height: 16px; background: var(--brand-blue);
  }
  .front-brand .brand-name {
    font-size: 18px; font-weight: 600; color: var(--brand-blue); letter-spacing: 0.5px;
  }
  .contact {
    position: absolute; left: 288px; top: 108px;
  }
  .contact .person-name {
    font-size: 20px; font-weight: 400; color: var(--ink-light); line-height: 1.2;
  }
  .contact .job-title {
    font-size: 12px; font-weight: 600; color: var(--brand-deep); margin-top: 1px;
  }
  .contact-list { list-style: none; margin-top: 14px; }
  .contact-list li {
    display: flex; align-items: center; gap: 8px;
    font-size: 11.5px; color: var(--ink-muted); height: 21px;
  }
  .contact-list svg { width: 12px; height: 12px; fill: none; stroke: var(--brand-deep); stroke-width: 1.6; }

  .back-brand {
    position: absolute; left: 0; right: 0; top: 128px;
    display: flex; justify-content: center; align-items: center; gap: 14px;
  }
  .back-brand .brand-square { width: 40px; height: 40px; }
  .back-brand .brand-name {
    font-size: 54px; font-weight: 600; color: var(--brand-blue); letter-spacing: 1px; line-height: 1;
  }
</style>
</head>
<body>
  <section class="card card-front">
    <div class="front-brand">
      <span class="brand-square"></span>
      <span class="brand-name">KORVELTA</span>
    </div>
    <div class="contact">
      <p class="person-name">Your Name</p>
      <p class="job-title">Job Title</p>
      <ul class="contact-list">
        <li>
          <svg viewBox="0 0 12 12"><path d="M2 4c0-1.5 8-1.5 8 0v1H8V4H4v1H2z M3 6h6l1 4H2z"/></svg>
          000 000 0000
        </li>
        <li>
          <svg viewBox="0 0 12 12"><circle cx="6" cy="6" r="4.8"/><path d="M1.2 6h9.6 M6 1.2c-2.4 2.6-2.4 7 0 9.6 M6 1.2c2.4 2.6 2.4 7 0 9.6"/></svg>
          youremail@xyz.com
        </li>
        <li>
          <svg viewBox="0 0 12 12"><rect x="1" y="2.5" width="10" height="7"/><path d="M1 2.5l5 4 5-4"/></svg>
          www.korveltait.example
        </li>
      </ul>
    </div>
  </section>

  <section class="card card-back">
    <div class="back-brand">
      <span class="brand-square"></span>
      <span class="brand-name">KORVELTA</span>
    </div>
  </section>
</body>
</html>
```